Varno Building Pty Ltd need an Identity!

We need a logo design for a building company based in Sydney, Australia. In addition - Business Card Layout. The colour scheme is to be black and red and communicate a professional yet 'hands on' approach to building.

Target Market(s)

Architects, Home Owners, Developers

Industry/Entity Type

Construction

Font styles to use
Serif
Sans Serif

Colors
ec1f27

Requirements
Must have
• Clear logo and professional direction.
Nice to have
• Use of initials as a possible logo
Should not have
• Graphics/pictures of houses, house roofs etc. Can be an abstracted form of a building.

```html
<!DOCTYPE html>
<html lang="en">
<head>
<meta charset="utf-8">
<title>Varno Building Pty Ltd — Identity</title>
<link rel="stylesheet" href="https://fonts.googleapis.com/css2?family=Montserrat:wght@500;600;700&display=swap">
<style>
  :root {
    --brand-red: #a80f14;
    --ink: #111111;
    --card-black: #0d0d0d;
    --paper: #ffffff;
    --backdrop: #e9e6e2;
    --muted-light: #cfcfcf;
  }
  * { box-sizing: border-box; margin: 0; padding: 0; }
  html, body { width: 857px; height: 1200px; overflow: hidden; }
  body {
    background: var(--backdrop);
    font-family: "Montserrat", Arial, sans-serif;
    color: var(--ink);
    position: relative;
  }

  /* Logo sheet */
  .logo-sheet {
    position: absolute; left: 48px; top: 48px;
    width: 760px; height: 337px;
    background: var(--paper);
    box-shadow: 0 4px 14px rgba(0,0,0,.18);
  }
  .logo-sheet .swatches { position: absolute; left: 14px; top: 14px; display: flex; gap: 10px; }
  .swatch { width: 18px; height: 18px; }
  .swatch--black { background: var(--ink); }
  .swatch--red { background: var(--brand-red); }
  .logo-sheet .app-tile {
    position: absolute; right: 12px; top: 12px;
    width: 60px; height: 60px; border-radius: 9px; background: var(--brand-red);
  }
  .logo-sheet .wordmark-lockup {
    position: absolute; left: 0; right: 0; top: 140px;
    display: flex; justify-content: center; align-items: center; gap: 14px;
  }

  /* Wordmark */
  .wordmark-lockup { display: flex; align-items: center; }
  .wordmark-dot { border-radius: 50%; background: var(--brand-red); flex: none; }
  .wordmark {
    font-weight: 700; color: var(--ink); line-height: 1; letter-spacing: -0.5px;
  }
  .wordmark small { display: block; text-align: right; letter-spacing: 1px; margin-top: 3px; }
  .logo-sheet .wordmark-dot { width: 44px; height: 44px; }
  .logo-sheet .wordmark { font-size: 40px; }
  .logo-sheet .wordmark small { font-size: 12px; }

  /* Business card front */
  .card {
    position: absolute; width: 540px; height: 310px;
    box-shadow: 0 5px 16px rgba(0,0,0,.25);
  }
  .card--front { left: 48px; top: 430px; background: var(--paper); }
  .card--front .wordmark-lockup { position: absolute; left: 28px; top: 36px; gap: 10px; }
  .card--front .wordmark-dot { width: 30px; height: 30px; }
  .card--front .wordmark { font-size: 27px; }
  .card--front .wordmark small { font-size: 9px; }

  .name-band {
    position: absolute; left: 240px; right: 0; top: 104px; height: 38px;
    background: var(--brand-red); color: var(--paper);
    font-weight: 600; font-size: 19px; padding: 8px 8px;
  }
  .name-rule {
    position: absolute; left: 300px; right: 0; top: 148px; height: 4px; background: var(--ink);
  }
  .job-title { position: absolute; left: 248px; top: 146px; font-size: 13px; font-weight: 600; }
  .contact { position: absolute; left: 248px; top: 188px; font-size: 13px; font-weight: 600; line-height: 1.35; }
  .contact .label { color: var(--brand-red); }
  .address { position: absolute; left: 248px; top: 250px; font-size: 12.5px; font-weight: 600; line-height: 1.35; }
  .address .label { color: var(--brand-red); display: block; }

  /* Business card back */
  .card--back { left: 268px; top: 820px; background: var(--card-black); }
  .card--back .back-mark {
    position: absolute; left: 50%; top: 95px; transform: translateX(-50%);
    width: 68px; height: 68px; border-radius: 50%; background: var(--brand-red);
  }
  .card--back .website {
    position: absolute; left: 0; right: 0; top: 190px; text-align: center;
    color: var(--muted-light); font-weight: 600; font-size: 17px; letter-spacing: .3px;
  }
</style>
</head>
<body>
  <section class="logo-sheet" aria-label="Logo presentation">
    <div class="swatches">
      <span class="swatch swatch--black"></span>
      <span class="swatch swatch--red"></span>
    </div>
    <div class="app-tile"></div>
    <div class="wordmark-lockup">
      <span class="wordmark-dot"></span>
      <div class="wordmark">Varno Building<small>PTY LTD</small></div>
    </div>
  </section>

  <article class="card card--front" aria-label="Business card front">
    <div class="wordmark-lockup">
      <span class="wordmark-dot"></span>
      <div class="wordmark">Varno Building<small>PTY LTD</small></div>
    </div>
    <div class="name-band">Client Name</div>
    <div class="name-rule"></div>
    <p class="job-title">Owner</p>
    <p class="contact">
      <span class="label">Phone:</span> 000-000-0000<br>
      <span class="label">Email:</span> info@varnobuilding.com
    </p>
    <p class="address">
      <span class="label">Address:</span>
      Adress Line 1 Here<br>
      Address Line 2 Here
    </p>
  </article>

  <article class="card card--back" aria-label="Business card back">
    <div class="back-mark"></div>
    <p class="website">www.varnobuilding.com</p>
  </article>
</body>
</html>
```